Kestrel Vale - Multifamily Development

Kestrel Vale is a Luxury Multifamily Development project located in Orange, NJ. This project will be completed in three phases with the first phase about 75% complete. Each phase will have a different name as follows
ALDER Kestrel Vale
WILLOW Kestrel Vale
JUNIPERS Kestrel Vale
We are going to install a banner on the side of the first building which will act as advertising for all buildings. We will eventually need advertising that will be in the windows as well as marketing materials . We want the marketing for this project to be similar for all three phases. At the moment, we are starting with this first simple banner. Attached is a rough idea of the look as well as our color palette. If you feel the color palette is a little too monochrome, feel free to propose an accent color. You can also visit our website to see more info on our company as well as the project. www.tarnvx.com Finally, if you need AI files (ie. for the logo), we can send to you. Thanks..

```html
<!DOCTYPE html>
<html lang="en">
<head>
<meta charset="utf-8">
<title>ALDER Kestrel Vale – Building Banners</title>
<link href="https://fonts.googleapis.com/css2?family=Oswald:wght@300;400;600;700&family=Archivo+Black&family=Cinzel:wght@600;700&display=swap" rel="stylesheet">
<style>
  :root {
    --slate-blue: #44618a;
    --slate-deep: #3b5a81;
    --navy: #1b2538;
    --gold: #a88b6b;
    --white: #ffffff;
  }
  html, body {
    margin: 0;
    padding: 0;
    width: 1200px;
    height: 2187px;
    overflow: hidden;
    background: var(--white);
  }
  .banner-set { display: block; width: 1200px; height: 2187px; }
  .brand { font-family: "Oswald", sans-serif; font-weight: 700; fill: var(--navy); }
  .brand-sub { font-family: "Oswald", sans-serif; font-weight: 400; fill: var(--navy); }
  .project-name { font-family: "Oswald", sans-serif; font-weight: 700; fill: var(--white); }
  .project-sub { font-family: "Oswald", sans-serif; font-weight: 400; fill: var(--white); }
  .project-sub--bold { font-weight: 700; }
  .phone-digit { font-family: "Archivo Black", sans-serif; fill: var(--white); text-anchor: middle; }
  .tagline { font-family: "Cinzel", serif; font-weight: 700; fill: var(--white); }
  .tagline--gold { fill: var(--gold); }
  .web-address { font-family: "Oswald", sans-serif; font-weight: 300; fill: var(--white); }
  .field { fill: url(#fieldTone); }
  .panel-dark { fill: var(--navy); }
  .rule-dark { fill: var(--navy); }
  .rule-light { fill: var(--white); }
</style>
</head>
<body>
<svg class="banner-set" viewBox="0 0 1200 2187" xmlns="http://www.w3.org/2000/svg">
  <defs>
    <linearGradient id="fieldTone" x1="0" y1="0" x2="0" y2="1">
      <stop offset="0" stop-color="#44618a"/>
      <stop offset="0.5" stop-color="#3f5d86"/>
      <stop offset="1" stop-color="#44618a"/>
    </linearGradient>
  </defs>

  <!-- Banner A: wave top -->
  <g class="banner banner--wave">
    <path class="field" role="img" aria-label="Background area for a subtle angular blue pattern" d="M0,297 C0,332 60,344 210,342 C400,336 570,328 570,378 L570,2187 L0,2187 Z"/>

    <text class="brand" x="100" y="253" font-size="118" textLength="366" lengthAdjust="spacingAndGlyphs">TARNVX</text>
    <text class="brand-sub" x="100" y="299" font-size="34" textLength="372" lengthAdjust="spacingAndGlyphs">P R O P E R T I E S</text>

    <text class="project-name" x="104" y="503" font-size="152" textLength="349" lengthAdjust="spacingAndGlyphs">ALDER</text>
    <text class="project-sub" x="104" y="573" font-size="58" textLength="352" lengthAdjust="spacing">KESTREL</text>
    <text class="project-sub" x="104" y="635" font-size="58" textLength="352" lengthAdjust="spacing">VALE</text>

    <rect class="rule-dark" x="178" y="670" width="215" height="12"/>

    <g class="phone" font-size="108">
      <text class="phone-digit" x="286" y="787" textLength="83" lengthAdjust="spacingAndGlyphs">5</text>
      <text class="phone-digit" x="286" y="888" textLength="83" lengthAdjust="spacingAndGlyphs">5</text>
      <text class="phone-digit" x="286" y="983" textLength="83" lengthAdjust="spacingAndGlyphs">5</text>
      <rect class="rule-light" x="262" y="1000" width="39" height="6"/>
      <text class="phone-digit" x="286" y="1106" textLength="83" lengthAdjust="spacingAndGlyphs">0</text>
      <text class="phone-digit" x="286" y="1204" textLength="83" lengthAdjust="spacingAndGlyphs">1</text>
      <text class="phone-digit" x="286" y="1304" textLength="83" lengthAdjust="spacingAndGlyphs">4</text>
      <rect class="rule-light" x="262" y="1321" width="39" height="6"/>
      <text class="phone-digit" x="286" y="1423" textLength="83" lengthAdjust="spacingAndGlyphs">2</text>
      <text class="phone-digit" x="286" y="1523" textLength="83" lengthAdjust="spacingAndGlyphs">8</text>
      <text class="phone-digit" x="286" y="1621" textLength="83" lengthAdjust="spacingAndGlyphs">7</text>
      <text class="phone-digit" x="286" y="1719" textLength="83" lengthAdjust="spacingAndGlyphs">0</text>
    </g>

    <rect class="rule-dark" x="178" y="1744" width="215" height="12"/>

    <text class="tagline" x="136" y="1846" font-size="74" textLength="308" lengthAdjust="spacingAndGlyphs">LUXURY</text>
    <text class="tagline" x="62" y="1937" font-size="74" textLength="446" lengthAdjust="spacingAndGlyphs">APARTMENT</text>
    <text class="tagline" x="119" y="2027" font-size="74" textLength="336" lengthAdjust="spacingAndGlyphs">RENTALS</text>

    <rect class="rule-dark" x="245" y="2050" width="82" height="6"/>
    <text class="web-address" x="143" y="2110" font-size="62" textLength="287" lengthAdjust="spacingAndGlyphs">tarnvx.com</text>
  </g>

  <!-- Banner B: chamfered top with dark footer -->
  <g class="banner banner--chamfer">
    <polygon class="field" role="img" aria-label="Background area for a subtle angular blue pattern" points="723,352 1200,352 1200,2187 627,2187 627,446"/>

    <text class="brand" x="688" y="270" font-size="140" textLength="446" lengthAdjust="spacingAndGlyphs">TARNVX</text>
    <text class="brand-sub" x="688" y="325" font-size="42" textLength="454" lengthAdjust="spacingAndGlyphs">P R O P E R T I E S</text>

    <text class="project-name" x="740" y="509" font-size="152" textLength="348" lengthAdjust="spacingAndGlyphs">ALDER</text>
    <text class="project-sub project-sub--bold" x="740" y="577" font-size="54" textLength="352" lengthAdjust="spacing">KESTREL</text>
    <text class="project-sub" x="740" y="641" font-size="58" textLength="352" lengthAdjust="spacing">VALE</text>

    <rect class="rule-light" x="847" y="670" width="133" height="7"/>

    <g class="phone" font-size="108">
      <text class="phone-digit" x="913" y="787" textLength="83" lengthAdjust="spacingAndGlyphs">5</text>
      <text class="phone-digit" x="913" y="888" textLength="83" lengthAdjust="spacingAndGlyphs">5</text>
      <text class="phone-digit" x="913" y="983" textLength="83" lengthAdjust="spacingAndGlyphs">5</text>
      <rect class="rule-light" x="889" y="1000" width="39" height="6"/>
      <text class="phone-digit" x="913" y="1106" textLength="83" lengthAdjust="spacingAndGlyphs">0</text>
      <text class="phone-digit" x="913" y="1204" textLength="83" lengthAdjust="spacingAndGlyphs">1</text>
      <text class="phone-digit" x="913" y="1304" textLength="83" lengthAdjust="spacingAndGlyphs">4</text>
      <rect class="rule-light" x="889" y="1321" width="39" height="6"/>
      <text class="phone-digit" x="913" y="1423" textLength="83" lengthAdjust="spacingAndGlyphs">2</text>
      <text class="phone-digit" x="913" y="1523" textLength="83" lengthAdjust="spacingAndGlyphs">8</text>
      <text class="phone-digit" x="913" y="1621" textLength="83" lengthAdjust="spacingAndGlyphs">7</text>
      <text class="phone-digit" x="913" y="1719" textLength="83" lengthAdjust="spacingAndGlyphs">0</text>
    </g>

    <polygon class="panel-dark" points="723,1749 1104,1749 1200,1842 1200,2187 627,2187 627,1842"/>

    <text class="tagline tagline--gold" x="766" y="1851" font-size="76" textLength="310" lengthAdjust="spacingAndGlyphs">LUXURY</text>
    <text class="tagline tagline--gold" x="692" y="1940" font-size="76" textLength="446" lengthAdjust="spacingAndGlyphs">APARTMENT</text>
    <text class="tagline tagline--gold" x="749" y="2029" font-size="76" textLength="336" lengthAdjust="spacingAndGlyphs">RENTALS</text>

    <rect class="rule-light" x="872" y="2057" width="83" height="7"/>
    <text class="web-address" x="773" y="2135" font-size="58" textLength="282" lengthAdjust="spacingAndGlyphs">TARNVX.COM</text>
  </g>
</svg>
</body>
</html>
```